PVTR - Label for a lifestyle beer for gamers

We are launching a lifestyle brewery for gamers. Our first beer is called PVTR (the same as the company) and we are launching a promo campaign showcasing a bunch of possible design directions for it, which our community can then vote for. The top 5 (or more) labels of this competition will be selected as winners and be part of that campaign. If one of them is chosen by the community, we will continue that work with the chosen designer.

So feel free to come up with a specific game genre, target group (described in the attachment) or style for your submission. Or a specific market (such as a Korvaxi inspired beer for the japanese market) We encourage diversity among the submissions.

Full description in the attached document.

Target Market(s)

Gamers of all ages

Requirements
Nice to have
• All kinds of gaming references or graphical choices inspired by gaming

```html
<!DOCTYPE html>
<html lang="en">
<head>
<meta charset="utf-8">
<title>PVTR Pale Ale – Label Directions</title>
<link href="https://fonts.googleapis.com/css2?family=Bebas+Neue&family=Oswald:wght@500&family=Silkscreen:wght@400;700&display=swap" rel="stylesheet">
<style>
  :root {
    --paper: #ffffff;
    --band: #f58f20;
    --amber: #fbb01c;
    --gold: #fcc814;
    --glow: #fdee21;
    --hop: #f7a029;
    --brand-blue: #2b5eab;
    --navy: #2b2f7a;
    --ink: #111111;
    --white: #ffffff;
  }
  * { box-sizing: border-box; margin: 0; padding: 0; }
  html, body { width: 1200px; height: 1046px; overflow: hidden; background: var(--paper); }
  .canvas { position: relative; width: 1200px; height: 1046px; }

  .label {
    position: absolute; top: 34px; width: 533px; height: 980px; overflow: hidden;
  }
  .label--classic { left: 45px;
    background: radial-gradient(circle at 62% 52%, var(--glow) 0%, #fcd01d 30%, var(--amber) 75%);
  }
  .label--pixel { left: 626px; background: var(--gold); }

  .label__band { position: absolute; top: 0; left: 0; width: 100%; height: 29px; background: var(--band); }
  .label__skyline { position: absolute; top: 29px; left: 0; width: 100%; height: 520px; }

  .decor { position: absolute; background: var(--hop); opacity: .28; border-radius: 40% 40% 45% 45%; }

  .brand {
    position: absolute; top: 250px; left: 0; width: 100%; text-align: center;
    font-family: "Bebas Neue", sans-serif; font-size: 170px; line-height: 1;
    color: var(--brand-blue); letter-spacing: 10px;
  }
  .label--pixel .brand { font-family: "Silkscreen", sans-serif; font-weight: 700; font-size: 128px; top: 265px; letter-spacing: 0; }

  .tagline {
    position: absolute; top: 426px; left: 0; width: 100%; text-align: center;
    font-family: "Silkscreen", sans-serif; font-weight: 700; font-size: 19px;
    color: var(--white); word-spacing: 8px; letter-spacing: 1px; white-space: nowrap;
  }

  .style-name {
    position: absolute; left: 0; width: 100%; text-align: center; color: var(--white);
  }
  .label--classic .style-name__line1 {
    top: 580px; font-family: "Bebas Neue", sans-serif; font-size: 96px; line-height: 1;
    letter-spacing: 2px; text-shadow: 5px 5px 0 var(--navy);
  }
  .label--classic .style-name__line2 {
    top: 668px; font-family: "Bebas Neue", sans-serif; font-size: 152px; line-height: 1;
    letter-spacing: 22px; padding-left: 22px; text-shadow: 6px 6px 0 var(--navy);
  }
  .label--pixel .style-name__line1 {
    top: 582px; font-family: "Silkscreen", sans-serif; font-weight: 700; font-size: 64px; line-height: 1;
    text-shadow: 5px 5px 0 var(--navy);
  }
  .label--pixel .style-name__line2 {
    top: 660px; font-family: "Silkscreen", sans-serif; font-weight: 700; font-size: 118px; line-height: 1;
    text-shadow: 6px 6px 0 var(--navy);
  }

  .abv {
    position: absolute; top: 904px; left: 0; width: 100%; text-align: center;
    font-family: "Oswald", sans-serif; font-weight: 500; font-size: 28px; letter-spacing: 3px; color: var(--ink);
  }
  .label--pixel .abv { color: var(--navy); font-size: 31px; }
</style>
</head>
<body>
<main class="canvas">

  <section class="label label--classic" aria-label="Pale ale label, classic type direction">
    <div class="label__band"></div>
    <div class="decor" role="img" aria-label="hop cone illustration" style="left:440px;top:80px;width:90px;height:140px"></div>
    <div class="decor" role="img" aria-label="beer mug illustration" style="left:0;top:120px;width:70px;height:120px"></div>
    <div class="decor" role="img" aria-label="hop cone illustration" style="left:0;top:320px;width:55px;height:130px"></div>
    <div class="decor" role="img" aria-label="hop cone illustration" style="left:465px;top:465px;width:68px;height:150px"></div>
    <div class="decor" role="img" aria-label="beer mug illustration" style="left:0;top:530px;width:100px;height:150px"></div>
    <div class="decor" role="img" aria-label="beer mug illustration" style="left:460px;top:670px;width:73px;height:150px"></div>
    <div class="decor" role="img" aria-label="hop cone illustration" style="left:0;top:730px;width:75px;height:140px"></div>
    <div class="brand">PVTR</div>
    <p class="tagline">Press Start To Play</p>
    <p class="style-name style-name__line1">PALE ALE</p>
    <p class="style-name style-name__line2">BEER</p>
    <p class="abv">13.37% ABV./VOL</p>
  </section>

  <section class="label label--pixel" aria-label="Pale ale label, pixel type direction">
    <svg class="label__skyline" viewBox="0 0 533 520" preserveAspectRatio="none" aria-hidden="true">
      <path fill="var(--amber)" d="M0 0H533V423H533V423H505V450H455V470H430V450H385V495H358V470H305V513H270V470H240V450H185V490H155V455H115V485H70V455H55V513H30V455H0Z"/>
    </svg>
    <div class="label__band"></div>
    <div class="decor" role="img" aria-label="hop cone illustration" style="left:440px;top:80px;width:90px;height:140px"></div>
    <div class="decor" role="img" aria-label="beer mug illustration" style="left:0;top:120px;width:70px;height:120px"></div>
    <div class="decor" role="img" aria-label="hop cone illustration" style="left:465px;top:465px;width:68px;height:150px"></div>
    <div class="decor" role="img" aria-label="beer mug illustration" style="left:0;top:530px;width:100px;height:150px"></div>
    <div class="decor" role="img" aria-label="beer mug illustration" style="left:460px;top:670px;width:73px;height:150px"></div>
    <div class="decor" role="img" aria-label="hop cone illustration" style="left:0;top:730px;width:75px;height:140px"></div>
    <div class="brand">PVTR</div>
    <p class="tagline">Press Start To Play</p>
    <p class="style-name style-name__line1">PALE ALE</p>
    <p class="style-name style-name__line2">BEER</p>
    <p class="abv">13.37% ABV./VOL</p>
  </section>

</main>
</body>
</html>
```